Updated Business Card Design more modern and eye catching

looking for something more dynamic than the sterile card we have now. Please take a look at our web site www.brindlemarket.net to see what we do. only looking for the front side of the card for now. I've also attached a sample of a card with raised spot uv ink - it might be cool to incorporate something like that. Card should be bold yet serious. No frilly or scrolly stuff on it.
Updates
Target Market(s)
We do decor and signage for retail business and supermarkets. Our new name should reflect that we're hip but serious.
Contact Information for Business Card
standard business card size - horizontal preferred
Font styles to use
Requirements
Must have
- Current logo and colors cannot be changed.
Nice to have
- Must have information shown on existing card but open to some changes. Okay to consider spot uv.
Should not have
- Not busy with pictures in the background.

```html
<!DOCTYPE html>
<html lang="en">
<head>
<meta charset="utf-8">
<title>Brindle Market – Business Card</title>
<link rel="stylesheet" href="https://fonts.googleapis.com/css2?family=Lora:wght@400;700&display=swap">
<style>
  :root {
    --stage: #262626;
    --card-dark: #1f1f1f;
    --card-light: #ffffff;
    --gold: #b5a447;
    --gold-light: #c9b960;
    --ink: #2b2b2b;
    --white: #ffffff;
  }
  * { margin: 0; padding: 0; box-sizing: border-box; }
  html, body {
    width: 1200px; height: 895px; overflow: hidden;
    background: var(--stage);
  }
  .card {
    position: absolute; left: 180px; top: 207px;
    width: 840px; height: 480px;
    background: var(--card-dark);
    overflow: hidden;
    box-shadow: 0 20px 40px rgba(0,0,0,.5);
    font-family: "Lora", serif;
  }
  .info-panel {
    position: absolute; left: 0; top: 0;
    width: 390px; height: 100%;
    background: var(--card-light);
    padding: 58px 0 0 44px;
  }
  .person-name {
    font-weight: 700; font-size: 32px; color: var(--gold);
    letter-spacing: .5px; line-height: 1; white-space: nowrap;
  }
  .person-title {
    font-size: 17px; color: var(--ink); margin-top: 6px; margin-left: 22px;
  }
  .title-rule {
    width: 80px; height: 3px; background: var(--gold);
    margin: 8px 0 0 40px;
  }
  .contact-list { list-style: none; margin-top: 84px; margin-left: 80px; }
  .contact-list li {
    display: flex; align-items: center; gap: 14px;
    font-size: 18px; color: var(--ink); height: 30px; white-space: nowrap;
  }
  .contact-list svg { width: 16px; height: 16px; flex: none; }
  .gold-band {
    position: absolute; left: 0; top: 0; width: 840px; height: 480px;
  }
  .address {
    position: absolute; left: 390px; top: 385px;
    width: 410px; text-align: center; white-space: nowrap;
    font-size: 18px; color: var(--white); letter-spacing: .3px;
  }
  .logo-square {
    position: absolute; right: 58px; top: 40px;
    width: 78px; height: 78px; border: 4px solid var(--gold);
  }
  .brand-name {
    position: absolute; right: 50px; top: 214px;
    font-size: 36px; font-weight: 400; color: var(--white);
    letter-spacing: 5px; text-transform: uppercase; line-height: 1;
    white-space: nowrap;
  }
</style>
</head>
<body>
  <div class="card">
    <section class="info-panel">
      <h1 class="person-name">MARLA OSTRAND</h1>
      <p class="person-title">Vice-President</p>
      <div class="title-rule"></div>
      <ul class="contact-list">
        <li><svg viewBox="0 0 16 16" aria-hidden="true"><rect x="4" y="1" width="8" height="14" rx="1.5" fill="none" stroke="#b5a447" stroke-width="1.6"/></svg>555.210.4471</li>
        <li><svg viewBox="0 0 16 16" aria-hidden="true"><path d="M3 2l3 0 1 3-2 1.5c1 2 2.5 3.5 4.5 4.5L11 9l3 1 0 3c-6 1-12-5-11-11z" fill="#b5a447"/></svg>555.308.1920 ext.3</li>
        <li><svg viewBox="0 0 16 16" aria-hidden="true"><rect x="1.5" y="3.5" width="13" height="9" fill="none" stroke="#b5a447" stroke-width="1.6"/><path d="M1.5 3.5l6.5 5 6.5-5" fill="none" stroke="#b5a447" stroke-width="1.6"/></svg>marla@brindlemarket.net</li>
        <li><svg viewBox="0 0 16 16" aria-hidden="true"><circle cx="8" cy="6.5" r="4.5" fill="none" stroke="#b5a447" stroke-width="1.8"/><path d="M5 10.5l-3 4" stroke="#b5a447" stroke-width="1.8"/></svg>www.brindlemarket.net</li>
      </ul>
    </section>

    <svg class="gold-band" viewBox="0 0 840 480" aria-hidden="true">
      <polygon points="0,376 840,376 840,420 0,420" fill="var(--gold)"/>
      <polygon points="0,420 60,420 80,448 0,448" fill="var(--gold-light)"/>
      <polygon points="770,376 840,376 840,348 790,348" fill="var(--gold-light)"/>
    </svg>
    <p class="address">4120 Commerce Way Dr. Harbor Point, FL 30417</p>

    <div class="logo-square"></div>
    <p class="brand-name">Brindle Market</p>
  </div>
</body>
</html>
```